Bright Harbour Electrical Limited needs advertisement brochure

We require a brochure with details of the services we provide. We have just become the only approved installer for RVL products on the Isle of Man and want to feature their producst heavily in the brochure centre pages. We estimate it will be 8 pages of A5 and we would like it to be landscape please. We have all the required content as per the word doc attached and just need it to be made to look professional. It doesn't need to include all the attached pictures and only certain information from the RVL brochure needs to be included (i.e the first couple of pages of write up).
Front Page - Just the Bright Harbour main logo and pics of vans
Page 2 - About us and the logos for who we are approved by (Kelby Traders Guild etc)
Page 3 - Domestic Electrical Services as per the word doc attached (those pictures don't have to be used so if you find better ones please go ahead and use).
Page 4 & 5 (Centre Pages) RVL information. Please make it clear that we are the only approved installers of their products on the Isle of Man.
Page 6 & 7 - Commercial Services as per the word doc attached (again if you can find better pictures than the ones contained in the word doc then feel free to use).
Page 8 - Back page to contain all our contact information.

Target Market(s)

Domestic and commercial customers. A design install and maintain company. Facility maintenance, preventative maintenance, fire alarm and emergency lighting contracts, home automation and sound system. Project management.

Industry/Entity Type

Electrical

Requirements
Must have
• Must be professional and appeal to both domestic and commercial customers. Has to be "BRIGHT" "EARTHY GREEN GLOBAL FEEL" like our logo shows. "CREATIVE" design. Possible similarity to our letter headed paper with part of the green globe down one side of the brochure. Must use Carlos Sanz text which is the Varnel Quist text same as logo. Snazzy looking, eye catching, appealing. Everything you would want to get new business in the door.
Nice to have
• As above
Should not have
• Over the top tacky earthy look. After all we also wire houses that are run by horrible oil boilers (no option). Don't want to put all my egg in one basket kind of thing.

```html
<!DOCTYPE html>
<html lang="en">
<head>
<meta charset="utf-8">
<title>Bright Harbour Electrical – Brochure Centre Spread</title>
<link href="https://fonts.googleapis.com/css2?family=Open+Sans:wght@300;400;600&display=swap" rel="stylesheet">
<style>
  :root{
    --bg:#d9d9d9;
    --forest:#0f2a17;
    --forest-deep:#0a1f10;
    --leaf:#2fa84a;
    --leaf-bright:#43c25a;
    --paper:#ffffff;
    --paper-shade:#eeeeee;
    --ink:#3a3a3a;
    --ink-soft:#6a6a6a;
    --on-dark:#cfd8d1;
  }
  *{box-sizing:border-box;margin:0;padding:0}
  html,body{width:1200px;height:935px;overflow:hidden}
  body{background:var(--bg);font-family:"Open Sans",Arial,sans-serif;color:var(--ink)}
  .spread{position:absolute;left:20px;top:255px;width:1160px;height:412px;display:flex;box-shadow:0 8px 24px rgba(0,0,0,.25)}
  .page{position:relative;width:580px;height:412px;overflow:hidden;background:var(--paper)}
  .page--left::after{content:"";position:absolute;right:0;top:0;width:30px;height:100%;background:linear-gradient(to left,rgba(0,0,0,.12),transparent)}
  .page--right::before{content:"";position:absolute;left:0;top:0;width:30px;height:100%;background:linear-gradient(to right,rgba(0,0,0,.1),transparent);z-index:3}

  /* left page */
  .overview{position:absolute;left:0;top:0;width:262px;height:100%;background:linear-gradient(160deg,var(--forest) 0%,var(--forest-deep) 100%);padding:46px 22px 0 24px;color:var(--on-dark)}
  .overview h2{font-weight:300;font-size:21px;color:var(--leaf-bright);padding-bottom:8px;border-bottom:1px solid rgba(255,255,255,.25);margin-bottom:10px}
  .overview p{font-size:8.4px;line-height:1.5;margin-bottom:9px;font-weight:300}
  .web{position:absolute;font-size:8.5px;letter-spacing:1.5px;color:var(--leaf-bright)}
  .overview .web{left:24px;bottom:18px}
  .brand{position:absolute;left:262px;width:318px;top:28px;text-align:center}
  .brand__mark{width:58px;height:58px;border-radius:50%;background:var(--leaf);margin:0 auto 10px}
  .brand__name{font-size:19px;font-weight:400;letter-spacing:1px;color:var(--ink)}
  .brand__sub{font-size:9px;color:var(--ink-soft);margin-top:2px}
  .photo{position:absolute;border-radius:3px}
  .photo--range{left:300px;top:150px;width:250px;height:180px;background:radial-gradient(ellipse at 55% 55%,#e6e6e6 0%,#bdbdbd 55%,#f4f4f4 100%)}
  .page-num{position:absolute;width:16px;height:16px;background:var(--forest);border:1px solid var(--leaf);color:#fff;font-size:8px;display:flex;align-items:center;justify-content:center;transform:rotate(45deg)}
  .page-num span{transform:rotate(-45deg)}
  .page--left .page-num{right:40px;bottom:48px;z-index:2}
  .band{position:absolute;left:0;bottom:0;width:100%;height:70px}

  /* right page */
  .hero{position:absolute;left:0;top:0;width:100%;height:232px;background:linear-gradient(to bottom,var(--paper) 60%,var(--paper-shade))}
  .photo--unit{left:36px;top:40px;width:200px;height:168px;background:radial-gradient(ellipse at 50% 50%,#cfcfd2 0%,#a9a9ad 55%,#efefef 100%)}
  .product{position:absolute;left:262px;top:30px;width:292px}
  .product h1{font-weight:300;font-size:30px;color:var(--leaf);letter-spacing:1px;line-height:1}
  .product h3{font-weight:300;font-size:13px;color:var(--ink);margin:4px 0 10px}
  .product p{font-size:8.4px;line-height:1.55;color:var(--ink)}
  .product .approved{margin-top:6px;font-weight:600;color:var(--leaf)}
  .features{position:absolute;left:0;top:232px;width:100%;height:180px;background:linear-gradient(160deg,var(--forest) 0%,var(--forest-deep) 100%);color:var(--on-dark)}
  .features__rule{position:absolute;left:0;top:-6px;width:100%;height:14px}
  .features h2{position:absolute;left:36px;top:30px;font-weight:300;font-size:19px;color:var(--leaf-bright)}
  .features ul{position:absolute;list-style:none;font-size:8.4px;line-height:1.75;font-weight:300}
  .features ul li::before{content:"• ";color:var(--leaf-bright)}
  .features .col-a{left:36px;top:62px}
  .features .col-b{left:300px;top:38px}
  .features .web{left:36px;bottom:16px}
  .page--right .page-num{right:26px;top:16px}
</style>
</head>
<body>
<main class="spread">
  <section class="page page--left">
    <div class="overview">
      <h2>Product Overview</h2>
      <p>The basis behind all of our product designs is that they are all flexible heating solutions. Marketed under 'The FlexHeat' concept this allows multiple heat sources to be successfully integrated and future-proof any installation. At the heart of the FlexHeat concept is the ThermaCore, our innovative, high performance thermal store incorporating intelligent control.</p>
      <p>This concept is based on an environmentally friendly, economical and flexible heating system with the RVL ThermaCore thermal store at the heart of the installation. By then connecting this to one of our heat pumps or biomass boilers you are prepared for the future. By installing ThermaCore your heating system will prove to be both efficient and effective. In a world of changing energy supply, the flexibility of FlexHeat allows you to ensure that your system is ready and able to adapt to these future changes.</p>
      <p>FlexHeat is pre-programmed to take control of all your heating equipment both now and in the future. All you need to do is connect, control, enjoy and save money.</p>
      <div class="web">www.brightharbour-electrical.im</div>
    </div>

    <div class="brand">
      <div class="brand__mark"></div>
      <div class="brand__name">BRIGHT HARBOUR</div>
      <div class="brand__sub">Electrical Limited</div>
    </div>

    <div class="photo photo--range" role="img" aria-label="Photo of the RVL product range: thermal store cylinders, solar panel and air source heat pump"></div>

    <svg class="band" viewBox="0 0 580 70" preserveAspectRatio="none" aria-hidden="true">
      <path d="M262 70 L262 52 Q420 30 580 18 L580 70 Z" fill="#0f2a17"/>
      <path d="M0 58 Q300 52 580 14 L580 22 Q300 62 0 66 Z" fill="#2fa84a"/>
    </svg>
    <div class="page-num"><span>1</span></div>
  </section>

  <section class="page page--right">
    <div class="hero">
      <div class="photo photo--unit" role="img" aria-label="Photo of the AeroVane 400 air source heat pump unit"></div>
      <div class="product">
        <h1>AEROVANE 400</h1>
        <h3>Air Source Heat Pump Range</h3>
        <p>RVL's AeroVane 400 range of air source heat pumps offer an extremely efficient solution for space heating and hot water generation helping to reduce heating costs by as much as 70%. Absorbing energy from the air and using it to generate heat for all types of domestic property. The unit can operate at outside air temperatures of -22°C and still generate useful energy. Stylish, discrete and designed to fit into most external environments.</p>
        <p class="approved">Bright Harbour is the only approved installer of RVL products on the Isle of Man.</p>
      </div>
    </div>
    <div class="features">
      <svg class="features__rule" viewBox="0 0 580 14" preserveAspectRatio="none" aria-hidden="true">
        <path d="M0 14 Q300 2 580 6 L580 10 Q300 6 0 14 Z" fill="#2fa84a"/>
      </svg>
      <h2>Key features</h2>
      <ul class="col-a">
        <li>High efficiency with a COP of over 4.6 at A7/W35</li>
        <li>Electronic expansion valve</li>
        <li>On demand defrosting</li>
        <li>Operates in temperatures as low as -22°C</li>
        <li>Produces DHW temperatures up to 65°C</li>
      </ul>
      <ul class="col-b">
        <li>Significantly reduces heating costs</li>
        <li>Wide range of outputs up to 20kW</li>
        <li>Low noise operation</li>
        <li>Built in Smart Start technology to reduce peak currents</li>
        <li>Condensation tray with built in heater</li>
      </ul>
      <div class="web">www.brightharbour-electrical.im</div>
      <div class="page-num"><span>2</span></div>
    </div>
  </section>
</main>
</body>
</html>
```